Web design for a Crane & Heavy Equipment Inspection, Repair and Maintenance Company in Texas

We need a web design for a new company based in Houston, Texas called "Kelder Crane & Equipment". We inspect, repair and maintain diesel driven heavy equipment, generators, fire water pumps and cranes. We would like to see designs that use the colors orange, white, yellow and brown, and/or orange, white, navy, yellow and grey.

```html
<!DOCTYPE html>
<html lang="en">
<head>
<meta charset="utf-8">
<title>Kelder Crane &amp; Equipment</title>
<link rel="stylesheet" href="https://fonts.googleapis.com/css2?family=Play:wght@400;700&family=Arimo:ital,wght@0,400;0,700;1,400&display=swap">
<style>
:root{
  --orange:#ef5a2a;
  --orange-dark:#e4501f;
  --navy:#1d4a78;
  --ink:#333;
  --grey:#666;
  --line:#d6d6d6;
  --white:#fff;
}
*{margin:0;padding:0;box-sizing:border-box}
html,body{width:791px;height:1200px;overflow:hidden;background:var(--white)}
body{position:relative;font-family:"Arimo",Arial,sans-serif;color:var(--ink)}
.abs{position:absolute}
.top-rule{left:0;top:12px;width:791px;height:1px;background:#ececec}
.brand{left:80px;top:58px;display:flex;align-items:center;gap:8px}
.brand-dot{width:14px;height:14px;border-radius:50%;background:var(--orange)}
.brand-name{font-family:"Play",sans-serif;font-weight:700;font-size:21px;color:var(--navy);letter-spacing:.2px}
.nav{left:439px;top:79px;display:flex;align-items:center;font-size:10px;color:var(--grey)}
.nav a{color:inherit;text-decoration:none;position:relative}
.nav .home{background:var(--orange);color:var(--white);border-radius:4px;width:49px;height:22px;display:flex;align-items:center;justify-content:center;margin-right:16px}
.nav .about{margin-right:18px}
.nav .about::after{content:"";position:absolute;left:15px;top:18px;border:4px solid transparent;border-top:5px solid #444}
.nav .services{margin-right:23px}
.nav .blogs{margin-right:21px}
.hero{left:1px;top:126px;width:790px;height:352px;background:linear-gradient(90deg,#b7542a 0%,#c98a63 22%,#9fb0c4 38%,#4a6f96 48%,#c7d0da 62%,#b9c3cd 72%,#e2672f 86%,#8a8f97 100%)}
.hero-caption{left:1px;top:411px;width:790px;height:46px;background:rgba(30,30,30,.72)}
.hero-caption p{position:absolute;left:87px;top:15px;width:510px;color:var(--white);font-size:11.5px;line-height:16px;top:15px;margin-top:-1px}
.dot{width:12px;height:12px;border-radius:50%;background:var(--white);top:435px}
.dot.on{background:var(--orange)}
.service{width:190px;text-align:center}
.service .icon{width:70px;height:70px;border-radius:50%;background:var(--orange);margin:0 auto;display:flex;align-items:center;justify-content:center}
.service h2{font-family:"Play",sans-serif;font-weight:400;font-size:17px;color:var(--navy);margin:21px 0 8px}
.service p{font-size:9px;line-height:11px;color:var(--grey);padding:0 12px}
.btn{display:flex;align-items:center;justify-content:center;background:var(--orange);color:var(--white);font-size:9.5px;border-radius:4px;text-decoration:none}
.service .btn{width:76px;height:32px;margin:17px auto 0}
.section-title{font-family:"Play",sans-serif;font-weight:700;font-size:17px;color:var(--navy)}
.welcome-text{left:79px;top:823px;width:344px;font-size:8.6px;line-height:11px;color:var(--grey);text-align:justify}
.photo{background:linear-gradient(135deg,#8d7a45,#c9a13a 45%,#6c7480)}
.divider{left:456px;top:787px;width:1px;height:223px;background:var(--line)}
.quote{left:493px;width:222px;border:1px solid var(--line);border-radius:4px;padding:7px 6px;font-size:8.6px;line-height:11px;color:var(--grey);text-align:justify;background:var(--white)}
.quote::after{content:"";position:absolute;right:24px;bottom:-9px;width:14px;height:14px;background:var(--white);border-right:1px solid var(--line);border-bottom:1px solid var(--line);transform:rotate(45deg) skew(8deg,8deg)}
.quote-name{right:86px;font-size:9px;font-weight:700;color:#222}
.more-link{right:74px;top:1002px;font-size:8.6px;font-style:italic;color:var(--orange)}
.call{left:0;top:1066px;width:791px;text-align:center;font-size:16px;font-style:italic;color:var(--navy)}
.call span{color:var(--orange)}
.footer{left:0;top:1096px;width:791px;height:104px;background:var(--orange-dark)}
.footer-links{left:84px;top:1108px;font-size:7.5px;color:var(--white)}
.footer-links span{margin:0 3px}
.copyright{left:84px;top:1126px;font-size:7.5px;color:var(--white)}
.follow{left:634px;top:1102px;font-size:9px;color:var(--white)}
.social{width:22px;height:22px;border-radius:50%;background:var(--white);top:1118px}
</style>
</head>
<body>
<div class="abs top-rule"></div>

<header>
  <div class="abs brand"><span class="brand-dot"></span><span class="brand-name">Kelder Crane &amp; Equipment</span></div>
  <nav class="abs nav">
    <a class="home" href="#">Home</a>
    <a class="about" href="#">About Us</a>
    <a class="services" href="#">Services</a>
    <a class="blogs" href="#">Blogs</a>
    <a href="#">Contact Us</a>
  </nav>
</header>

<section>
  <div class="abs hero" role="img" aria-label="Photo of a crane lifting a blue shipping container beside an engineer in a hard hat and high-visibility jacket"></div>
  <div class="abs hero-caption"><p>Loremipsum dolor sit amet, dui a, massarutrummaurisarcuaugueamet ac, in maurisnislnatoque, odiovivamusquisque mi ac portanonummy, proinarcucurabitur. Sagittistellusleomorbi in quam.</p></div>
  <span class="abs dot on" style="left:593px"></span>
  <span class="abs dot" style="left:613px"></span>
  <span class="abs dot" style="left:633px"></span>
</section>

<section>
  <div class="abs service" style="left:74px;top:520px">
    <div class="icon"><svg width="36" height="36" viewBox="0 0 36 36" fill="none" stroke="#fff" stroke-width="3"><circle cx="21" cy="13" r="7"/><path d="M15 18l-8 6"/><path d="M5 30h26v-6" stroke-linejoin="round"/></svg></div>
    <h2 style="margin-top:24px">Inspection</h2>
    <p>Nullam bibendum at nulla, coaccusan felis teru tempu in. Cras in semper yllelacualls. Donecti vitae egeststi sapien.</p>
    <a class="btn" href="#">Read More</a>
  </div>
  <div class="abs service" style="left:294px;top:520px">
    <div class="icon"><svg width="34" height="34" viewBox="0 0 34 34" fill="none" stroke="#fff" stroke-width="3.5" stroke-linecap="round"><path d="M8 8l18 18"/><path d="M26 8L8 26"/><circle cx="8" cy="8" r="3" fill="#fff"/><path d="M23 5l6 6"/></svg></div>
    <h2 style="margin-top:13px">Repairing</h2>
    <p>Nullam bibendum at nulla, coaccusan felis teru tempu in. Cras in semper yllelacualls. Donecti vitae egeststi sapien.</p>
    <a class="btn" href="#">Read More</a>
  </div>
  <div class="abs service" style="left:525px;top:518px">
    <div class="icon"><svg width="44" height="34" viewBox="0 0 44 34" fill="none" stroke="#fff"><circle cx="15" cy="19" r="7" stroke-width="5" stroke-dasharray="3 2.5"/><circle cx="15" cy="19" r="3" stroke-width="2"/><circle cx="32" cy="12" r="5" stroke-width="4" stroke-dasharray="2.5 2"/><circle cx="32" cy="12" r="2" stroke-width="1.5"/></svg></div>
    <h2 style="margin-top:15px">Maintenance</h2>
    <p>Nullam bibendum at nulla, coaccusan felis teru tempu in. Cras in semper yllelacualls. Donecti vitae egeststi sapien.</p>
    <a class="btn" href="#">Read More</a>
  </div>
</section>

<section>
  <h2 class="abs section-title" style="left:79px;top:786px">Welcome to Kelder Crane &amp; Equipment</h2>
  <p class="abs welcome-text">Kelder Crane and Equipment Services Company, LLC provides on-site crane, generator and heavy equipment repair, maintenance and inspection. Our commitment to our clients extends beyond our core values of safety, honesty, quality and reliability. We are leveraging technology to improve our clients' access to inspection, maintenance and repair records.</p>
  <div class="abs photo" style="left:79px;top:892px;width:133px;height:89px" role="img" aria-label="Photo of two workers in hard hats inspecting equipment in a workshop"></div>
  <div class="abs photo" style="left:236px;top:892px;width:128px;height:90px;background:linear-gradient(135deg,#5d6168,#a9abae 50%,#d8a030)" role="img" aria-label="Photo of a technician in a hard hat repairing machinery"></div>
  <a class="abs btn" href="#" style="left:79px;top:1000px;width:68px;height:23px">Read More</a>
</section>

<div class="abs divider"></div>

<aside>
  <h2 class="abs section-title" style="left:493px;top:786px">Testimonials</h2>
  <blockquote class="abs quote" style="top:817px;height:48px">“Lorem ipsum dolor sits amet, consectetur adipiscing elit. Quid sequatur, quid repugnet, vident. Duo Reges: constructio interrete. ”</blockquote>
  <p class="abs quote-name" style="top:885px">Dale R. Whitcomb</p>
  <blockquote class="abs quote" style="top:913px;height:49px">“Lorem ipsum dolor sits amet, consectetur adipiscing elit. Quid sequatur, quid repugnet, vident. Duo Reges: constructio interrete. ”</blockquote>
  <p class="abs quote-name" style="top:983px">Luis Ortega</p>
  <a class="abs more-link" href="#">Read more testimonials...</a>
</aside>

<p class="abs call">For Service &amp; Inspections Call: <span>832.555.0147</span></p>

<footer>
  <div class="abs footer"></div>
  <p class="abs footer-links">Home<span>:</span>About Us<span>:</span>Services<span>:</span>Testimonials<span>:</span>Contact Us</p>
  <p class="abs copyright">Copyright © 2014 Kelder Crane &amp; Equipment Services Company, LLC</p>
  <p class="abs follow">Follow Us</p>
  <span class="abs social" style="left:634px" aria-label="Social profile"></span>
  <span class="abs social" style="left:661px" aria-label="Social profile"></span>
</footer>
</body>
</html>
```